I already have a business sign that has what I want on my business cards, however it needs to be modified to make a double sided business card. Also the wording needs modification. I want the Corvella Tennis Coaching logo on the front of the business card with the Black/Green background. And I want the tennis ball dot points on the back of the card with the green background. The dot points as follows:
-All Ages Welcome
-Qualified, Enthusiastic Coaches
-Group, Semi Private & Private Lessons
-Beginner, Intermediate and Advanced Standards
-Velmora Rally
-Kestrel Kids

Also, I want the "A GREAT WAY TO GET FIT AND HEALTHY" to remain as is, and my name and number.
I've added a file that has my current signage, as a guide.

```html
<!DOCTYPE html>
<html lang="en">
<head>
<meta charset="utf-8">
<title>Corvella Tennis Coaching – Business Card</title>
<link rel="stylesheet" href="https://fonts.googleapis.com/css2?family=Exo+2:ital,wght@0,400;0,600;0,700;0,800;1,800&display=swap">
<style>
  :root {
    --bg: #e7e9e2;
    --lime-light: #d2e85a;
    --lime: #b6d634;
    --lime-deep: #8fb51c;
    --band-dark: #141514;
    --band-mid: #2b2d2b;
    --ink: #1b1d17;
    --silver: #eef1f3;
    --rule: rgba(40, 50, 20, 0.35);
  }
  * { box-sizing: border-box; margin: 0; padding: 0; }
  html, body {
    width: 1200px;
    height: 1023px;
    overflow: hidden;
    background: var(--bg);
    font-family: "Exo 2", sans-serif;
  }
  .sheet {
    position: relative;
    width: 1200px;
    height: 1023px;
    display: flex;
    flex-direction: column;
    align-items: center;
    justify-content: center;
    gap: 70px;
  }
  .card {
    position: relative;
    width: 600px;
    height: 343px;
    border-radius: 22px;
    overflow: hidden;
    background: linear-gradient(160deg, var(--lime-light) 0%, var(--lime) 55%, var(--lime-deep) 100%);
    box-shadow: 0 6px 18px rgba(0, 0, 0, 0.18);
  }

  /* Front */
  .front-band {
    position: absolute;
    left: 0;
    top: 38px;
    width: 100%;
    height: 112px;
    background: linear-gradient(180deg, var(--band-mid) 0%, var(--band-dark) 100%);
    display: flex;
    align-items: center;
    justify-content: center;
    gap: 16px;
  }
  .brand-dot {
    width: 40px;
    height: 40px;
    border-radius: 50%;
    background: var(--lime);
    flex: none;
  }
  .brand-name {
    font-weight: 700;
    font-size: 34px;
    letter-spacing: 0.5px;
    color: var(--silver);
  }
  .contact {
    position: absolute;
    left: 0;
    top: 168px;
    width: 100%;
    text-align: center;
    color: var(--ink);
  }
  .contact-name {
    font-weight: 800;
    font-size: 27px;
    letter-spacing: 1.5px;
    color: #ffffff;
    text-shadow: 0 1px 2px rgba(0, 0, 0, 0.55);
  }
  .contact-phone {
    margin-top: 4px;
    font-size: 19px;
    font-weight: 600;
  }
  .contact-rule {
    width: 78%;
    height: 1px;
    margin: 8px auto 6px;
    background: var(--rule);
  }
  .contact-web {
    font-size: 17px;
    font-weight: 400;
  }
  .tagline {
    position: absolute;
    left: 0;
    bottom: 0;
    width: 100%;
    height: 44px;
    background: var(--band-dark);
    display: flex;
    align-items: center;
    justify-content: center;
    font-weight: 800;
    font-style: italic;
    font-size: 19px;
    letter-spacing: 1px;
    color: var(--lime-light);
  }

  /* Back */
  .back-brand {
    position: absolute;
    left: 34px;
    top: 30px;
    display: flex;
    align-items: center;
    gap: 12px;
  }
  .back-brand .brand-name { color: var(--ink); font-size: 28px; }
  .back-brand .brand-dot { width: 30px; height: 30px; background: var(--band-dark); }
  .points {
    position: absolute;
    left: 46px;
    top: 98px;
    list-style: none;
    color: var(--ink);
  }
  .point {
    display: flex;
    align-items: center;
    gap: 14px;
    font-size: 19px;
    font-weight: 600;
    line-height: 37px;
  }
  .point-ball { flex: none; }
</style>
</head>
<body>
<main class="sheet">

  <section class="card card-front" aria-label="Business card front">
    <div class="front-band">
      <span class="brand-dot"></span>
      <span class="brand-name">Corvella Tennis Coaching</span>
    </div>
    <div class="contact">
      <p class="contact-name">DANE HARLOW</p>
      <p class="contact-phone">0400 555 218</p>
      <div class="contact-rule"></div>
      <p class="contact-web">www.corvellatenniscoaching.com.au</p>
    </div>
    <p class="tagline">A GREAT WAY TO GET FIT AND HEALTHY</p>
  </section>

  <section class="card card-back" aria-label="Business card back">
    <div class="back-brand">
      <span class="brand-dot"></span>
      <span class="brand-name">Corvella Tennis Coaching</span>
    </div>
    <ul class="points">
      <li class="point"><svg class="point-ball" width="16" height="16" viewBox="0 0 16 16"><circle cx="8" cy="8" r="7" fill="#1b1d17"/><path d="M3 3.5 Q8 8 3 12.5 M13 3.5 Q8 8 13 12.5" stroke="#b6d634" stroke-width="1.2" fill="none"/></svg>All Ages Welcome</li>
      <li class="point"><svg class="point-ball" width="16" height="16" viewBox="0 0 16 16"><circle cx="8" cy="8" r="7" fill="#1b1d17"/><path d="M3 3.5 Q8 8 3 12.5 M13 3.5 Q8 8 13 12.5" stroke="#b6d634" stroke-width="1.2" fill="none"/></svg>Qualified, Enthusiastic Coaches</li>
      <li class="point"><svg class="point-ball" width="16" height="16" viewBox="0 0 16 16"><circle cx="8" cy="8" r="7" fill="#1b1d17"/><path d="M3 3.5 Q8 8 3 12.5 M13 3.5 Q8 8 13 12.5" stroke="#b6d634" stroke-width="1.2" fill="none"/></svg>Group, Semi Private &amp; Private Lessons</li>
      <li class="point"><svg class="point-ball" width="16" height="16" viewBox="0 0 16 16"><circle cx="8" cy="8" r="7" fill="#1b1d17"/><path d="M3 3.5 Q8 8 3 12.5 M13 3.5 Q8 8 13 12.5" stroke="#b6d634" stroke-width="1.2" fill="none"/></svg>Beginner, Intermediate and Advanced Standards</li>
      <li class="point"><svg class="point-ball" width="16" height="16" viewBox="0 0 16 16"><circle cx="8" cy="8" r="7" fill="#1b1d17"/><path d="M3 3.5 Q8 8 3 12.5 M13 3.5 Q8 8 13 12.5" stroke="#b6d634" stroke-width="1.2" fill="none"/></svg>Velmora Rally</li>
      <li class="point"><svg class="point-ball" width="16" height="16" viewBox="0 0 16 16"><circle cx="8" cy="8" r="7" fill="#1b1d17"/><path d="M3 3.5 Q8 8 3 12.5 M13 3.5 Q8 8 13 12.5" stroke="#b6d634" stroke-width="1.2" fill="none"/></svg>Kestrel Kids</li>
    </ul>
  </section>

</main>
</body>
</html>
```